Yoga for Scoliosis business card/logo design

I need a business card/logo design for my new business. I am a registered yoga teacher and am certified in yoga for scoliosis. I'd like my card to read "Marlow Yoga Yoga for a Healthy Spine" and would like to incorporate one of the letters in my name{ ie the first vertical line of the letter " H "or "D"} to resemble a scoliotic spine. I regularly teach the following:Yoga for Scoliosis, Yoga for Back Health, Hatha yoga, Vinyasa yoga with Iyengar style alignment. This business is mostly for private clients, but I also teach group, semi-private & work shop classes. I like the colors green (light emerald) and royal blue. I'd like the design to be somewhat sleek, but not too modern. I also like the idea of a ying/yang symbol with a scoliotic spine dviding it.

Industry/Entity Type

Teacher

Contact Information for Business Card

Tamsin Marlow
200 RYT, Certified Yoga for Scoliosis Instructor
MarlowYoga.example
MarlowYoga@mailbox.example
415-629-3174

```html
<!DOCTYPE html>
<html lang="en">
<head>
<meta charset="utf-8">
<title>Marlow Yoga – Business Card</title>
<link href="https://fonts.googleapis.com/css2?family=Lato:ital,wght@0,400;1,400&display=swap" rel="stylesheet">
<style>
  :root {
    --page: #ffffff;
    --sky: #00b1ee;
    --azure: #0a72c4;
    --royal: #2a439c;
    --violet: #3b2f79;
    --night: #0a0a36;
    --emerald: #1eaa55;
    --sun: #ffe800;
    --ink: #1e1e1e;
    --sage: #6f9c7c;
    --phone: #1f7a48;
    --white: #ffffff;
  }
  * { margin: 0; padding: 0; box-sizing: border-box; }
  html, body {
    width: 1200px; height: 1200px; overflow: hidden;
    background: var(--page);
    font-family: "Lato", Arial, sans-serif;
  }
  .card {
    position: absolute;
    left: 248px; top: 372px;
    width: 751px; height: 340px;
  }
  .banner {
    position: absolute; left: 0; top: 0;
    width: 100%; height: 303px;
    background: linear-gradient(to bottom,
      var(--sky) 0%, var(--azure) 32%, var(--royal) 58%,
      var(--violet) 78%, var(--night) 100%);
  }
  .accent-stripe {
    position: absolute; left: 0; top: 303px;
    width: 100%; height: 11px;
    background: linear-gradient(to right, var(--emerald) 0%, var(--emerald) 45%, var(--sun) 100%);
  }
  .brand {
    position: absolute; left: 0; top: 0; width: 100%;
    text-align: center; color: var(--white); font-weight: 400;
  }
  .brand-name-top {
    position: absolute; left: 0; width: 100%; top: 46px;
    font-size: 46px; line-height: 1; letter-spacing: 30px; padding-left: 30px;
  }
  .brand-name-main {
    position: absolute; left: 0; width: 100%; top: 92px;
    font-size: 150px; line-height: 1; letter-spacing: 2px;
  }
  .tagline {
    position: absolute; left: 0; width: 100%; top: 232px;
    padding-left: 120px;
    text-align: center; color: var(--white);
    font-style: italic; font-size: 27px;
  }
  .holder {
    position: absolute; left: 33px; top: 328px;
  }
  .holder-name { font-size: 25px; color: var(--ink); letter-spacing: 0.5px; }
  .holder-credential {
    font-style: italic; font-size: 19px; color: var(--sage); margin-top: 8px; line-height: 1.55;
  }
  .contact {
    position: absolute; right: 27px; top: 328px; text-align: right;
  }
  .contact-phone { font-size: 26px; color: var(--phone); }
  .contact-line { font-size: 19px; color: var(--ink); margin-top: 8px; letter-spacing: 0.3px; }
  .contact-line + .contact-line { margin-top: 6px; }
</style>
</head>
<body>
  <div class="card">
    <div class="banner">
      <div class="brand">
        <div class="brand-name-top">MARLOW</div>
        <div class="brand-name-main">YOGA</div>
      </div>
      <div class="tagline">Yoga for a healthy spine</div>
    </div>
    <div class="accent-stripe"></div>

    <div class="holder">
      <div class="holder-name">TAMSIN MARLOW</div>
      <div class="holder-credential">200 RYT<br>Certified Yoga for Scoliosis Instructor</div>
    </div>

    <div class="contact">
      <div class="contact-phone">415-629-3174</div>
      <div class="contact-line">MARLOWYOGA.EXAMPLE</div>
      <div class="contact-line">MARLOWYOGA@MAILBOX.EXAMPLE</div>
    </div>
  </div>
</body>
</html>
```